Startup Drone Platform Company business card

We are needing a business card design for our employees. We are a startup drone platform. We are looking for a business card that has our logo on one side, with the employee/company details on the opposite side. We are looking for something that is very eye catching, modern, and bold.

Target Market(s)

This will target both drone pilots and drone businesses, along with all the industries that could utilize drone services (aerial video, aerial photos, inspections, 3d mapping, etc).

Industry/Entity Type

Business

```html
<!DOCTYPE html>
<html lang="en">
<head>
<meta charset="utf-8">
<title>Aerofleet Works – Business Card</title>
<link href="https://fonts.googleapis.com/css2?family=Questrial&display=swap" rel="stylesheet">
<style>
  :root {
    --backdrop: #5a4a3b;
    --brand-teal: #43c5d2;
    --card-white: #ffffff;
    --ink: #1a1a1a;
    --ink-soft: #555555;
  }
  * { margin: 0; padding: 0; box-sizing: border-box; }
  html, body {
    width: 1200px;
    height: 987px;
    overflow: hidden;
  }
  body {
    position: relative;
    background: var(--backdrop);
    font-family: "Questrial", "Century Gothic", sans-serif;
  }
  .card {
    position: absolute;
    left: 293px;
    width: 615px;
    height: 352px;
    overflow: hidden;
    box-shadow: 0 2px 6px rgba(0, 0, 0, 0.35);
  }
  .card--front {
    top: 125px;
    background: var(--brand-teal);
    color: var(--card-white);
  }
  .card--back {
    top: 510px;
    background: var(--card-white);
    color: var(--ink);
  }
  .front-ring {
    position: absolute;
    left: 0;
    top: 0;
    width: 615px;
    height: 352px;
  }
  .contact {
    position: absolute;
    left: 40px;
    top: 28px;
  }
  .contact__name {
    font-size: 26px;
    line-height: 1.1;
    font-weight: 400;
  }
  .contact__role {
    font-size: 18px;
    line-height: 1.25;
    margin-bottom: 12px;
  }
  .contact__address,
  .contact__lines {
    font-size: 16.5px;
    line-height: 1.28;
  }
  .contact__address { margin-bottom: 7px; }
  .brand {
    position: absolute;
    left: 0;
    right: 0;
    top: 82px;
    display: flex;
    flex-direction: column;
    align-items: center;
  }
  .brand__dot {
    width: 94px;
    height: 94px;
    border: 3px solid var(--brand-teal);
    border-radius: 50%;
    margin-bottom: 50px;
  }
  .brand__name {
    font-size: 21px;
    letter-spacing: 0.3em;
    text-transform: uppercase;
    padding-left: 0.3em;
  }
  .brand__url {
    position: absolute;
    left: 0;
    right: 0;
    top: 300px;
    text-align: center;
    font-size: 17px;
    letter-spacing: 0.14em;
    color: var(--ink-soft);
  }
</style>
</head>
<body>
  <section class="card card--front" aria-label="Card front">
    <svg class="front-ring" viewBox="0 0 615 352" aria-hidden="true">
      <circle cx="500" cy="250" r="175" fill="none" stroke="#ffffff" stroke-width="16"/>
    </svg>
    <div class="contact">
      <h1 class="contact__name">Daniel Reyes</h1>
      <p class="contact__role">CEO/Founder</p>
      <p class="contact__address">4120 Birchwood Drive<br>Fairbanks, Alaska 99701</p>
      <p class="contact__lines">P. 555 214 7730 C. 555 390 6182<br>hello@aerofleetworks.com<br>www.aerofleetworks.com</p>
    </div>
  </section>

  <section class="card card--back" aria-label="Card back">
    <div class="brand">
      <span class="brand__dot" aria-hidden="true"></span>
      <p class="brand__name">Aerofleet Works</p>
    </div>
    <p class="brand__url">www.aerofleetworks.com</p>
  </section>
</body>
</html>
```